Design a styled business card for an intimacy and attachment psychologist

I am a Psychologist providing online therapy to patients across the United States. My work is interpersonal and emotion-focused, with an emphasis on the client-therapist relationship. My primary areas of work are very personal, including sexuality and gender, abuse and trauma, and grief and loss. My target audience will be adults of all ages 18+.
My business card should convey a warm and inviting feeling of professionalism that is also casual and comfortable.
The front should be fairly simple and professional, consisting of:
- My name, Dr. Rosalind Petrakis
- My title, Licensed Psycholigist
- My logo
On either the front or the back, my contact information should be listed:
- ros@drrospetrakis.example
- 555.014.7788
- drrospetrakis.example
On the rear, I would like a description of the areas that I specialize in. This can be formatted in any way that appears stylistically interesting.
Individual and Couples
Relationships and Infidelity
Sexual Health & Aging
Gender Identity & Sexual Orientation
Abuse and Trauma
Sexual Compulsivity & Addiction
Sexual Dysfunction
Target Market(s)
My target audience will be adults of all ages 18+.
Industry/Entity Type
Psychology
Contact Information for Business Card
The front should be fairly simple and professional, consisting of: - My name, Dr. Rosalind Petrakis - My title, Licensed Psycholigist - My logo On either the front or the back, my contact information should be listed: - ros@drrospetrakis.example - 555.014.7788 - drrospetrakis.example On the rear, I would like a description of the areas that I specialize in. This can be formatted in any way that appears stylistically interesting. Individual and Couples Relationships and Infidelity Sexual Health & Aging Gender Identity & Sexual Orientation Abuse and Trauma Sexual Compulsivity & Addiction Sexual Dysfunction
- Follow brand guide

```html
<!DOCTYPE html>
<html lang="en">
<head>
<meta charset="utf-8">
<title>Dr. Rosalind Petrakis — Business Card</title>
<link href="https://fonts.googleapis.com/css2?family=Raleway:wght@400;500;600&display=swap" rel="stylesheet">
<style>
  :root {
    --backdrop: #d9d9d9;
    --navy: #29244a;
    --plum: #9b4fa0;
    --mint: #8fd0c0;
    --white: #ffffff;
    --ink: #1f1d2b;
  }
  * { box-sizing: border-box; margin: 0; padding: 0; }
  html, body {
    width: 1029px; height: 1200px; overflow: hidden;
    background: var(--backdrop);
    font-family: "Raleway", sans-serif;
  }
  .card {
    position: absolute;
    width: 620px; height: 352px;
    border-radius: 22px;
    overflow: hidden;
  }
  .card--front { left: 204px; top: 201px; background: var(--navy); }
  .card--back  { left: 205px; top: 675px; background: var(--white); }

  .identity {
    position: absolute; right: 41px; top: 56px; text-align: right;
  }
  .identity__name {
    color: var(--plum); font-weight: 600; font-size: 22px; letter-spacing: 0.1px;
  }
  .identity__title {
    color: var(--white); font-weight: 400; font-size: 16px; margin-top: 9px;
  }

  .brand { position: absolute; display: flex; align-items: center; }
  .brand__dot { border-radius: 50%; flex: none; background: var(--mint); }
  .brand__name { font-weight: 600; line-height: 1.2; }

  .card--front .brand { left: 42px; top: 205px; }
  .card--front .brand__dot { width: 86px; height: 86px; margin-right: 28px; }
  .card--front .brand__name { color: var(--white); font-size: 26px; }

  .card--back .brand { left: 38px; top: 37px; }
  .card--back .brand__dot { width: 76px; height: 76px; margin-right: 28px; }
  .card--back .brand__name { color: var(--ink); font-size: 23px; }

  .contacts { position: absolute; left: 357px; top: 140px; list-style: none; }
  .contacts li {
    display: flex; align-items: center; height: 24px; margin-bottom: 16px;
    font-size: 17px; color: var(--ink);
  }
  .contacts li:nth-child(2) { margin-bottom: 17px; }
  .contacts svg { width: 20px; height: 20px; margin-right: 10px; flex: none; }

  .specialties {
    position: absolute; left: 0; right: 0; top: 273px;
    text-align: center; font-size: 12.6px; font-weight: 500;
    color: var(--ink); line-height: 16.8px;
  }
</style>
</head>
<body>

<section class="card card--front">
  <div class="identity">
    <p class="identity__name">Dr. Rosalind Petrakis</p>
    <p class="identity__title">Licensed Psycholigist</p>
  </div>
  <div class="brand">
    <span class="brand__dot"></span>
    <p class="brand__name">Dr. Rosalind<br>Petrakis</p>
  </div>
</section>

<section class="card card--back">
  <div class="brand">
    <span class="brand__dot"></span>
    <p class="brand__name">Dr. Rosalind<br>Petrakis</p>
  </div>

  <ul class="contacts">
    <li>
      <svg viewBox="0 0 20 20" aria-hidden="true"><circle cx="10" cy="10" r="10" fill="#9b4fa0"/><path d="M7 5.5l1.6 2.2-.9 1.2c.6 1.3 1.5 2.2 2.8 2.8l1.2-.9 2.2 1.6-.7 1.6c-3.9-.3-7-3.4-7.3-7.3z" fill="#fff"/></svg>
      555.014.7788
    </li>
    <li>
      <svg viewBox="0 0 20 20" aria-hidden="true"><circle cx="10" cy="10" r="10" fill="#9b4fa0"/><rect x="5.2" y="6.6" width="9.6" height="6.8" rx="0.6" fill="#fff"/><path d="M5.6 7l4.4 3.4L14.4 7" fill="none" stroke="#9b4fa0" stroke-width="0.9"/></svg>
      ros@drrospetrakis.example
    </li>
    <li>
      <svg viewBox="0 0 20 20" aria-hidden="true"><circle cx="10" cy="10" r="10" fill="#9b4fa0"/><g fill="none" stroke="#fff" stroke-width="0.9"><circle cx="10" cy="10" r="5"/><ellipse cx="10" cy="10" rx="2.2" ry="5"/><path d="M5 10h10M5.8 7.5h8.4M5.8 12.5h8.4"/></g></svg>
      drrospetrakis.example
    </li>
  </ul>

  <p class="specialties">
    Stylistically Interesting | Individual and Couples | Relationships and Infidelity<br>
    Sexual Health &amp; Aging | Gender Identity &amp; Sexual Orientation | Abuse and Trauma<br>
    | Sexual Compulsivity &amp; Addiction | Sexual Dysfunction
  </p>
</section>

</body>
</html>
```